Ablaufgrafik KlickWerkstatt
Zielgruppe
KlickWerkstatt: Content Marketing-Lösung für KMU
Ohne Aufwand verleiht KlickWerkstatt Inhalten (Produkt-Meldungen, Presse-Mitteilungen, Blog-Artikel, …) die notwendige Reichweite um Neukundenkontakte zu generieren.
Der Content geht über alle Kanäle: Web, Mail und Social.
Der KlickWerkstatt bietet flexible und maßgeschneiderte Online Marketing Lösungen, die sich am Bedarf hinsichtlich Quantität, Qualität, den Kunden-Bedürfnissen und dem Budget angleichen. Bis hin zu individuell selektierten Verteilern.
Aufgabenstellung
Es soll eine Ablaufgrafik erstellt werden, die visualisiert "Was passiert mit meinem Content über den KlickWerkstatt": Eine Prozess-Visualisierung.
Die Ablaufgrafik wird als JPG/PNG bei klickwerkstatt.de eingebunden: Mit klick öffnet sich eine bildschirmfüllende Grafik. Ebenso soll die Grafik im factsheet (pdf) eingebunden werden.
- CI gemäß www.klickwerkstatt.de
- Anschauung und Info: factsheet-PDF http://kurzlink-beispiel.de/Rw7TqZ
- Logo: http://kurzlink-beispiel.de/Jm3VbK
Skizze zum Aufbau und den Inhalten für die Ablaufgrafik: s. Dateianlage (pdf)

```html
<!DOCTYPE html>
<html lang="de">
<head>
<meta charset="utf-8">
<title>Ablaufgrafik KlickWerkstatt</title>
<link href="https://fonts.googleapis.com/css2?family=Open+Sans:wght@300;400;600&display=swap" rel="stylesheet">
<style>
  :root {
    --dark: #3d434c;
    --sky: #56c2df;
    --teal: #64c2bd;
    --blue: #17a8da;
    --text: #4a4d52;
    --line: #dcdcdc;
    --white: #ffffff;
  }
  * { box-sizing: border-box; margin: 0; padding: 0; }
  html, body { width: 1200px; height: 2173px; overflow: hidden; background: var(--white); }
  body { position: relative; font-family: "Open Sans", Arial, sans-serif; color: var(--text); }
  .decor-area { position: absolute; left: 590px; top: 0; width: 610px; height: 630px;
    background: radial-gradient(ellipse at 85% 30%, rgba(23,168,218,0.85) 0%, rgba(100,194,189,0.6) 45%, rgba(255,255,255,0) 72%); }
  .connectors { position: absolute; left: 0; top: 0; }
  .brand { position: absolute; left: 101px; top: 74px; display: flex; align-items: center; gap: 14px; }
  .brand-mark { width: 40px; height: 40px; background: var(--blue); }
  .brand-name { font-size: 38px; font-weight: 400; color: var(--dark); letter-spacing: -0.5px; }
  .stage { position: absolute; left: 0; width: 374px; height: 67px; display: flex; }
  .stage-label { width: 295px; background: var(--dark); color: var(--white); font-size: 30px; font-weight: 400;
    display: flex; align-items: center; justify-content: center; letter-spacing: 0.5px; }
  .stage-accent { flex: 1; background: var(--sky); }
  .milestone { position: absolute; left: 481px; width: 232px; height: 57px; color: var(--white);
    background: linear-gradient(90deg, var(--teal), var(--blue)); font-size: 27px; font-weight: 600;
    display: flex; align-items: center; justify-content: center; }
  .node { position: absolute; background: var(--white); border: 2px solid var(--line); font-size: 21px;
    display: flex; align-items: center; justify-content: center; text-align: center; line-height: 1.35; }
  .node.tall { flex-direction: column; gap: 14px; }
  .channel { position: absolute; top: 949px; width: 164px; height: 164px; border-radius: 50%; background: var(--sky);
    color: var(--white); font-size: 28px; display: flex; flex-direction: column; align-items: center; justify-content: center; gap: 4px; }
  .channel svg { display: block; }
  .tagline { position: absolute; left: 373px; top: 2045px; width: 453px; height: 62px; border: 2px solid var(--line);
    background: var(--white); font-size: 22px; font-weight: 600; display: flex; align-items: center; justify-content: center; }
</style>
</head>
<body>

<div class="decor-area" role="img" aria-label="Dekorative Farbflächen in Türkis und Blau"></div>

<svg class="connectors" width="1200" height="2173" viewBox="0 0 1200 2173" aria-hidden="true"
     fill="none" stroke="#dcdcdc" stroke-width="2">
  <defs>
    <linearGradient id="people" gradientUnits="userSpaceOnUse" x1="224" y1="0" x2="973" y2="0">
      <stop offset="0" stop-color="#64c2bd"/><stop offset="1" stop-color="#17a8da"/>
    </linearGradient>
  </defs>
  <path d="M600 354 V415 M439 478 V415 H758 V478"/>
  <path d="M439 533 V602 M758 533 V602"/>
  <path d="M439 658 V721 H758 V658 M600 721 V782"/>
  <path d="M600 838 V895 M284 949 V895 H918 V949 M600 895 V949"/>
  <path d="M284 1113 V1180 M600 1113 V1180 M918 1113 V1180"/>
  <path d="M284 1273 V1292 M600 1354 V1373 M600 1435 V1454 M918 1242 V1261 M918 1324 V1342"/>
  <path d="M284 1354 V1560 H918 V1405 M600 1516 V1947"/>
  <path d="M600 2004 V2045"/>
  <g fill="url(#people)" stroke="none">
    <circle cx="261" cy="1768" r="37"/><circle cx="345" cy="1768" r="37"/><circle cx="430" cy="1768" r="37"/>
    <circle cx="514" cy="1768" r="37"/><circle cx="598" cy="1768" r="37"/><circle cx="683" cy="1768" r="37"/>
    <circle cx="767" cy="1768" r="37"/><circle cx="852" cy="1768" r="37"/><circle cx="936" cy="1768" r="37"/>
    <circle cx="261" cy="1852" r="37"/><circle cx="345" cy="1852" r="37"/><circle cx="430" cy="1852" r="37"/>
    <circle cx="514" cy="1852" r="37"/><circle cx="598" cy="1852" r="37"/><circle cx="683" cy="1852" r="37"/>
    <circle cx="767" cy="1852" r="37"/><circle cx="852" cy="1852" r="37"/><circle cx="936" cy="1852" r="37"/>
  </g>
  <g stroke="#ffffff" stroke-width="1.6" fill="none">
    <g id="user"><circle cx="261" cy="1762" r="8"/><path d="M245 1784 Q246 1772 255 1770 M277 1784 Q276 1772 267 1770 M245 1784 H277"/></g>
    <use href="#user" x="84"/><use href="#user" x="169"/><use href="#user" x="253"/><use href="#user" x="337"/>
    <use href="#user" x="422"/><use href="#user" x="506"/><use href="#user" x="591"/><use href="#user" x="675"/>
    <use href="#user" y="84"/><use href="#user" x="84" y="84"/><use href="#user" x="169" y="84"/><use href="#user" x="253" y="84"/>
    <use href="#user" x="337" y="84"/><use href="#user" x="422" y="84"/><use href="#user" x="506" y="84"/>
    <use href="#user" x="591" y="84"/><use href="#user" x="675" y="84"/>
  </g>
</svg>

<div class="brand"><span class="brand-mark"></span><span class="brand-name">KlickWerkstatt</span></div>

<div class="stage" style="top:293px"><div class="stage-label">ERSTELLEN</div><div class="stage-accent"></div></div>
<div class="stage" style="top:777px"><div class="stage-label">VERBREITEN</div><div class="stage-accent"></div></div>
<div class="stage" style="top:1611px"><div class="stage-label">AUSWERTEN</div><div class="stage-accent"></div></div>

<div class="milestone" style="top:298px">Ihre News</div>
<div class="node" style="left:323px;top:478px;width:177px;height:55px">Mail</div>
<div class="node" style="left:695px;top:478px;width:177px;height:55px">Login</div>
<div class="node" style="left:256px;top:602px;width:244px;height:56px">Einstellerservice</div>
<div class="node" style="left:695px;top:602px;width:264px;height:56px">Redaktionssystem</div>

<div class="milestone" style="top:782px">Ihr Newsroom</div>

<div class="channel" style="left:202px">
  <svg width="40" height="44" viewBox="0 0 40 44" aria-hidden="true"><path d="M4 2 L36 20 L22 24 L30 40 L24 42 L16 27 L8 38 Z" fill="#ffffff" stroke="#e0673a" stroke-width="2.5"/></svg>
  <span>Web</span>
</div>
<div class="channel" style="left:518px">
  <svg width="48" height="46" viewBox="0 0 48 46" aria-hidden="true"><path d="M2 18 L24 4 L46 18 V44 H2 Z" fill="#5b9aa8"/><rect x="8" y="8" width="32" height="26" fill="#ffffff"/><path d="M13 15 H27 M13 20 H35 M13 25 H35" stroke="#56c2df" stroke-width="2"/><path d="M2 18 L24 34 L46 18 V44 H2 Z" fill="#4a8a99"/></svg>
  <span>Mail</span>
</div>
<div class="channel" style="left:835px">
  <svg width="56" height="42" viewBox="0 0 56 42" aria-hidden="true"><path d="M18 12 H54 V32 H46 L44 40 L38 32 H18 Z" fill="#3d434c"/><path d="M2 2 H40 V26 H12 L6 32 V26 H2 Z" fill="#ffffff"/><path d="M8 9 H34 M8 14 H34 M8 19 H28" stroke="#56c2df" stroke-width="2"/></svg>
  <span>Social</span>
</div>

<div class="node" style="left:144px;top:1180px;width:269px;height:93px">Portale<br>im Medien-Netzwerk</div>
<div class="node" style="left:144px;top:1292px;width:269px;height:62px">Findmal &amp; Co.</div>

<div class="node tall" style="left:465px;top:1180px;width:269px;height:174px"><span>Marketing-Verteiler</span><span>Fach-/führungskräfte,<br>Entscheider,<br>Meinungsmacher, …</span></div>
<div class="node" style="left:465px;top:1373px;width:269px;height:62px">Journalisten-Verteiler</div>
<div class="node" style="left:465px;top:1454px;width:269px;height:62px">Individuelle-Verteiler</div>

<div class="node" style="left:786px;top:1180px;width:268px;height:62px">Nachbarnetz</div>
<div class="node" style="left:786px;top:1261px;width:268px;height:63px">Zwitscherfeed</div>
<div class="node" style="left:786px;top:1342px;width:268px;height:63px">Berufskontakt</div>

<div class="milestone" style="top:1947px">Ihre Firma</div>
<div class="tagline">Einfach. Erfolgreich. Kunden gewinnen.</div>

</body>
</html>
```